Sell the dream! Property investment proposal document

We are looking for a proposal document which outlines our vision for property development. The purpose of the document is to raise investment from investors - sell the dream!
Brief summary:
Tarrow Dwellings Developments, is an emerging New Zealand property investment company with a focus on providing unique property investment opportunities.
Our expertise and capabilities in architectural modular homes provide us with a remarkable advantage in tackling the development of properties that are typically considered challenging, remote, or uniquely positioned.
Our specialization in this niche sector of property development not only sets us apart from competitors, but also paves the way for lucrative investment opportunities in the New Zealand property market.
Feel free to use any images from www.tarrowdwellings.co.nz
Target Market(s)
investors for a unique property development opportunity
Industry/Entity Type
luxury property development in unique locations throughout New Zealand
Font styles to use
Colors
Designer to choose only greyscale colors for use in the design.
Look and feel

```html
<!DOCTYPE html>
<html lang="en">
<head>
<meta charset="utf-8">
<title>Tarrow Dwellings – Investment Proposal</title>
<link rel="stylesheet" href="https://fonts.googleapis.com/css2?family=Marcellus&family=Montserrat:wght@300;400;500&display=swap">
<style>
  :root{
    --ink:#2c2a2b;
    --sand:#bfb49b;
    --paper:#ffffff;
    --rule:#cfcfcf;
    --muted:#6b6b6b;
    --text-light:#f2efe9;
    --text-dark:#2c2a2b;
  }
  *{margin:0;padding:0;box-sizing:border-box}
  html,body{width:1200px;height:2343px;overflow:hidden;background:var(--paper)}
  body{position:relative;font-family:"Montserrat",sans-serif;color:var(--text-dark)}

  .board-header{position:absolute;left:49px;top:0;width:1102px;height:77px;border-bottom:1px solid var(--rule)}
  .board-header .client{position:absolute;right:0;top:46px;font-size:14px;font-weight:300;color:var(--muted);letter-spacing:.3px}
  .board-footer{position:absolute;left:0;top:2265px;width:1200px;border-top:1px solid var(--rule)}

  .page{position:absolute;overflow:hidden}
  .spread{position:absolute;width:728px;height:514px;overflow:hidden}
  .abs{position:absolute}

  .heading{font-family:"Marcellus",serif;font-weight:400;font-size:16.5px;line-height:1.15;letter-spacing:1px;text-transform:uppercase}
  .body-copy{font-size:5.8px;line-height:8.6px;font-weight:400}
  .body-copy p+p{margin-top:3px}
  .on-dark{color:var(--text-light)}
  .on-sand{color:var(--text-light)}

  .photo{position:absolute}

  /* cover */
  .cover{left:599px;top:114px;width:364px;height:513px;background:var(--ink)}
  .cover .photo{left:0;top:0;width:364px;height:256px;
    background:linear-gradient(180deg,#d9e2ea 0%,#c7d4de 28%,#6f8ea6 36%,#4f6f87 46%,#7e7a66 55%,#3a3533 70%,#1e1c1c 100%)}
  .cover .wordmark{left:38px;top:219px;font-family:"Montserrat",sans-serif;font-weight:300;font-size:66px;line-height:1;color:var(--paper);letter-spacing:-1px}
  .cover .tagline{left:99px;top:364px;font-size:15px;font-weight:300;line-height:20px;color:var(--text-light)}
  .cover .tagline span{display:block;padding-left:18px}
  .cover .signoff{right:42px;top:480px;font-size:8px;font-weight:400;color:var(--paper);letter-spacing:.5px}

  /* spread one */
  .spread-one{left:235px;top:648px}
  .overview{left:0;top:0;width:364px;height:514px;background:var(--sand)}
  .overview .photo{left:0;top:240px;width:364px;height:274px;
    background:linear-gradient(180deg,rgba(191,180,155,0) 0%,#a59e88 12%,#8a8773 26%,#6d6a4e 45%,#4f4c30 70%,#3a3726 100%)}
  .origins{left:364px;top:0;width:364px;height:514px;background:var(--ink)}
  .origins .img-a{left:203px;top:0;width:161px;height:225px;
    background:linear-gradient(180deg,#eef0f1 0%,#e4e6e6 50%,#3a3a38 58%,#4a4a40 78%,#8a8458 100%)}
  .origins .img-b{left:42px;top:225px;width:161px;height:124px;
    background:linear-gradient(180deg,#d8dadb 0%,#9aa3a8 35%,#6f7b55 60%,#5b4736 85%,#3a2e25 100%)}
  .origins .img-c{left:203px;top:349px;width:161px;height:165px;
    background:linear-gradient(180deg,#b6c1cc 0%,#d9c9ae 38%,#8d8a86 60%,#5d5c5a 80%,#77736d 100%)}

  /* spread two */
  .spread-two{left:235px;top:1184px;background:var(--ink)}
  .advantage-panel{left:21px;top:21px;width:322px;height:471px;
    background:linear-gradient(180deg,#f5f8fb 0%,#e9eef1 55%,#9da3a4 63%,#3a3a3a 70%,#6e8a3c 80%,#5a7a2c 100%)}
  .advantage-panel .heading{left:21px;top:65px;color:var(--text-dark)}
  .advantage-panel .body-copy{left:21px;top:105px;width:164px;font-size:6.1px;line-height:8.7px;color:var(--text-dark)}
  .spread-two .img-d{left:520px;top:0;width:208px;height:316px;
    background:linear-gradient(160deg,#aab0b2 0%,#8f8a78 30%,#6d6252 55%,#3c3a38 75%,#a7a29a 100%)}

  /* back cover */
  .back{left:235px;top:1719px;width:364px;height:514px;background:var(--ink)}
  .back .signoff{left:0;width:364px;top:248px;text-align:center;font-family:"Montserrat",sans-serif;font-weight:300;font-size:16px;letter-spacing:3px;color:var(--paper)}
</style>
</head>
<body>

<header class="board-header">
  <span class="client">Tarrow Dwellings</span>
</header>

<!-- front cover -->
<section class="page cover">
  <div class="photo" role="img" aria-label="Living room with lounge chairs facing a wide window over the ocean and hills"></div>
  <div class="abs wordmark">Tarrow</div>
  <p class="abs tagline">A Tarrow<span>to make your own.</span></p>
  <div class="abs signoff">Tarrow Dwellings</div>
</section>

<!-- spread: overview and origins -->
<section class="spread spread-one">
  <article class="abs overview">
    <div class="photo" role="img" aria-label="Dark modular homes on a grassy coastal hillside at dusk"></div>
    <h2 class="abs heading on-sand" style="left:42px;top:58px">Business<br>Overview</h2>
    <div class="abs body-copy on-sand" style="left:42px;top:100px;width:127px">
      <p>Tarrow Dwellings Developments, is an emerging New Zealand property investment company with a focus on providing unique property investment opportunities.</p>
      <p>Our expertise and capabilities in architectural modular homes provide us with a remarkable advantage in tackling the development of properties that are typically considered challenging, remote, or uniquely positioned.</p>
      <p>As a company, with 48 employees boasting a wealth of experience in handling complex architectural projects, making us well-equipped to navigate the intricacies and demands of such ventures.</p>
    </div>
    <div class="abs body-copy on-sand" style="left:193px;top:100px;width:130px">
      <p>This advantage allows us to not only execute projects efficiently but also to deliver exceptional results within condensed time frames.</p>
      <p>By capitalizing on our ability to develop difficult, remote, or one-of-a-kind properties swiftly and effectively, Tarrow Dwellings Developments offers investors a rare chance to engage in projects that promise exceptional profitability in the New Zealand property market.</p>
      <p>Our specialization in this niche sector of property development not only sets us apart from competitors, but also paves the way for lucrative investment opportunities in the New Zealand property market.</p>
    </div>
  </article>

  <article class="abs origins">
    <div class="photo img-a" role="img" aria-label="Dark pavilion home with glass walls set in tall grass"></div>
    <div class="photo img-b" role="img" aria-label="Interior with floor-to-ceiling windows looking over green hills"></div>
    <div class="photo img-c" role="img" aria-label="Glass home on a shoreline at sunset"></div>
    <h2 class="abs heading on-dark" style="left:42px;top:58px">Business<br>Origins</h2>
    <div class="abs body-copy on-dark" style="left:42px;top:112px;width:141px">
      <p>Tarrow Dwellings Developments was established with the goal of transforming the property investment market in New Zealand by introducing an innovative approach that centers on architectural modular designs and streamlined project timelines.</p>
      <p>Driven by our enthusiasm for architecture and real estate, we have expanded our successful business model to not only offer financial opportunities for investors but also to expand on our passion for high-end architectural design.</p>
    </div>
    <div class="abs body-copy on-dark" style="left:224px;top:257px;width:100px">
      <p>With a wealth of experience accumulated over the past six years in the construction and the property market, we are pivoting to focus solely on our property development initiatives, presenting completed Tarrow projects to the market, in exclusive locations.</p>
    </div>
    <div class="abs body-copy on-dark" style="left:42px;top:374px;width:138px">
      <p>These projects will boast high-quality standards, meticulous attention to detail and landscaping, and creative design elements.</p>
      <p>By introducing completed Tarrow properties into the market, we aim to reach a wider audience, catering to individuals who prefer ready-to-occupy homes, over engaging in the design and construction process. This approach also simplifies the financing process for prospective buyers, as established properties are often preferred by financial lenders.</p>
    </div>
  </article>
</section>

<!-- spread: advantage and financials -->
<section class="spread spread-two">
  <article class="abs advantage-panel" role="img" aria-label="Cantilevered dark home on a rocky green hillside above the sea">
    <h2 class="abs heading">Competitive<br>Advantage</h2>
    <div class="abs body-copy">
      <p>Our competitive advantage lies in the uniqueness of our property investment opportunities.</p>
      <p>Unlike traditional real estate companies, we focus on offering properties that are not only profitable but also aesthetically pleasing and unique. By catering to the tastes of architecture lovers, we set ourselves apart from the competition and attract a niche market of customers who appreciate the artistry and design of our projects.</p>
      <p>Additionally, the streamlined and condensed timelines facilitated by our modular approach provide quicker returns on investment.</p>
    </div>
  </article>
  <div class="photo img-d" role="img" aria-label="Corner interior with a lounge chair, hide rug and mountain views"></div>
  <h2 class="abs heading on-dark" style="left:406px;top:279px">Financial<br>Summary</h2>
  <div class="abs body-copy on-dark" style="left:406px;top:330px;width:138px">
    <p>In terms of financial projections, with each development, we anticipate a profit of 10%-20% which will be project dependent.</p>
    <p>This growth is fueled by the increasing demand for unique property investments in New Zealand and our ability to deliver high-quality services to the market in a condensed time frame, with heavily controlled costs.</p>
    <p>With a solid business model and a dedicated team, we are confident in our ability to achieve success and establish Tarrow Dwellings Investments as a trusted name in the industry.</p>
  </div>
  <div class="abs body-copy on-dark" style="left:557px;top:330px;width:138px">
    <p>New Zealand's property market has been experiencing steady growth over the years, making it an attractive destination for property investors. With its beautiful landscapes and strong economy, New Zealand offers a diverse range of investment opportunities for both local and international investors. The demand for quality properties in prime locations continues to rise, creating a favorable environment for property investment companies like ours that can lean on our modular benefits of being able to reach unique and remote locations.</p>
  </div>
</section>

<!-- back cover -->
<section class="page back">
  <div class="abs signoff">Tarrow</div>
</section>

<footer class="board-footer"></footer>

</body>
</html>
```